Business card and stationary for Intellectual Property Consultant & Law Firm
Harborline Claims Omniworks
Business card and stationary for Intellectual Property Consultant & Law Firm - Law
Creative Brief
Simple
Dorin Makalesu
President Director
Kelor Business Center 11th Floor Jl. Raya Wibisana Kav.37-38 Jakarta Pusat 10485, Indonesia
office@harborlineclaims.example
www.harborlineclaims.example
Member: OQRU, EKLM, UVBO, WDGF
Please add Intellectual Property Rights Consultant & Law Firm for letterhead additional of our email : hbl42@harborlineclaims.example; marks@harborlineclaims.example
please add Branch office : Surabaya (+6231) 480 3926 Medan (+6261) 819 4057 Solo (+62271) 634 918
trelvorin trelvorin
Dear All, Please provide me the stationary : letterhead, envelope, cds, ballpoint, ruler, stamps, usb sticks etc
dunmoral dunmoral
Please upload Ai or eps file of your logo thankyou
Please add : Intellectual Property Rights Consultant & Law Firm in envelope and letter head.

```html
<!DOCTYPE html>
<html lang="en">
<head>
<meta charset="utf-8">
<title>Harborline Claims Omniworks – Business Card</title>
<link href="https://fonts.googleapis.com/css2?family=Poppins:wght@400;500;600&display=swap" rel="stylesheet">
<style>
  :root {
    --backdrop: #e4e5e7;
    --card: #ffffff;
    --ink: #3b4049;
    --ink-soft: #6d727b;
    --accent: #f4a21d;
    --rule: #dfe1e4;
  }
  * { box-sizing: border-box; margin: 0; padding: 0; }
  html, body { width: 1200px; height: 883px; overflow: hidden; }
  body {
    background: var(--backdrop);
    font-family: "Poppins", sans-serif;
    color: var(--ink);
    position: relative;
  }
  .card {
    position: absolute;
    width: 500px;
    height: 286px;
    background: var(--card);
    border-radius: 22px;
    box-shadow: 0 10px 28px rgba(0,0,0,0.12);
  }
  .card--back { left: 640px; top: 160px; }
  .card--front { left: 80px; top: 440px; }

  .brand {
    display: flex;
    align-items: center;
    gap: 10px;
  }
  .brand__mark {
    width: 14px;
    height: 14px;
    background: var(--ink);
    flex: none;
  }
  .brand__name {
    font-weight: 600;
    color: var(--ink);
    line-height: 1.1;
  }
  .card--back .brand {
    position: absolute;
    left: 50%;
    top: 50%;
    transform: translate(-50%, -50%);
  }
  .card--back .brand__name { font-size: 26px; width: 250px; }
  .card--back .brand__mark { width: 20px; height: 20px; }

  .card--front .brand {
    position: absolute;
    right: 30px;
    top: 34px;
  }
  .card--front .brand__name { font-size: 19px; width: 190px; }

  .holder {
    position: absolute;
    left: 0;
    top: 92px;
    padding-left: 30px;
    border-left: 6px solid var(--accent);
  }
  .holder__name {
    font-size: 13px;
    font-weight: 500;
    letter-spacing: 0.06em;
    text-transform: uppercase;
  }
  .holder__title {
    font-size: 10px;
    color: var(--ink-soft);
  }

  .contacts {
    position: absolute;
    left: 36px;
    top: 150px;
    list-style: none;
  }
  .contacts li {
    display: flex;
    align-items: center;
    gap: 8px;
    font-size: 9px;
    color: var(--ink-soft);
    height: 20px;
  }
  .contacts svg { width: 11px; height: 11px; flex: none; }

  .address {
    position: absolute;
    right: 30px;
    top: 122px;
    text-align: right;
    font-size: 9.5px;
    line-height: 1.5;
    color: var(--ink-soft);
    font-style: normal;
  }
</style>
</head>
<body>

  <section class="card card--back" aria-label="Business card back">
    <div class="brand">
      <span class="brand__mark"></span>
      <span class="brand__name">Harborline Claims Omniworks</span>
    </div>
  </section>

  <section class="card card--front" aria-label="Business card front">
    <div class="brand">
      <span class="brand__mark"></span>
      <span class="brand__name">Harborline Claims Omniworks</span>
    </div>

    <div class="holder">
      <p class="holder__name">Tavin Orlesko</p>
      <p class="holder__title">Managing Director</p>
    </div>

    <ul class="contacts">
      <li>
        <svg viewBox="0 0 12 12"><path d="M3 1l2 2.5-1.2 1.2a6 6 0 0 0 3.5 3.5L8.5 7 11 9l-1.5 2C5 11 1 7 1 2.5z" fill="#6d727b"/></svg>
        (+6231) 480 3926
      </li>
      <li>
        <svg viewBox="0 0 12 12"><rect x="3" y="0.5" width="6" height="11" rx="1.2" fill="none" stroke="#6d727b" stroke-width="1.2"/><circle cx="6" cy="9.5" r="0.7" fill="#6d727b"/></svg>
        (+6261) 819 4057
      </li>
      <li>
        <svg viewBox="0 0 12 12"><rect x="1" y="4" width="10" height="6" rx="1" fill="#6d727b"/><rect x="3" y="1" width="6" height="3" fill="none" stroke="#6d727b" stroke-width="1"/></svg>
        (+62271) 634 918
      </li>
      <li>
        <svg viewBox="0 0 12 12"><rect x="0.8" y="2.3" width="10.4" height="7.4" rx="1" fill="none" stroke="#6d727b" stroke-width="1.1"/><path d="M1 3l5 3.6L11 3" fill="none" stroke="#6d727b" stroke-width="1.1"/></svg>
        office@harborlineclaims.example
      </li>
      <li>
        <svg viewBox="0 0 12 12"><circle cx="6" cy="6" r="5" fill="none" stroke="#6d727b" stroke-width="1.1"/><path d="M1 6h10M6 1c-2.5 3-2.5 7 0 10M6 1c2.5 3 2.5 7 0 10" fill="none" stroke="#6d727b" stroke-width="0.9"/></svg>
        www.harborlineclaims.example
      </li>
    </ul>

    <address class="address">
      Kelor Business Center 11th Floor<br>
      Jl. Raya Wibisana Kav.37-38
    </address>
  </section>

</body>
</html>
```